Packaging for Biscuit Moles (filled with chocolate!)

Who wouldn't want to eat a small cookie filed with creamy chocolate or vanilla?

This product is a cookie outside with a chocolate filling.

They are bite sized.

It will be a wrapper, 10cm by about 15cm (photo of one attached)

The product is called "Zizi Otter".

"Zizi Otter" does not have a logo. It just needs some sort of bubbly font that looks playful.

The elements I would like to retain:
Some form of a bear. I prefer one that looks much cuter!
The images of the actual cookie. (the bears with the drawings on them)
"Chocolate" or "Vanilla"

I look forward to your designs!

Some designs from other companies from other countries are attached.
Updates

I added a photo of my older pack.  I am looking for the "next generation" of this package.

It does not need to be completely different that this. I would like to just spruce up my old design.

OR, if you have a very cool idea, I'd love to see that as well!

Target Market(s)

Kids 5-20

Industry/Entity Type

Product

Requirements
Must have
• Attached are photos of the products, and the images of my current packaging.

The package will be a wrapper, as attached in another photo.

```html
<!DOCTYPE html>
<html lang="en">
<head>
<meta charset="utf-8">
<title>Zizi Otter – Biscuit Moles wrappers</title>
<link rel="stylesheet" href="https://fonts.googleapis.com/css2?family=Fredoka:wght@600&display=swap">
<style>
  :root {
    --canvas: #ffffff;
    --choc-pack: #d9634a;
    --choc-pack-edge: #c4533b;
    --vanilla-pack: #f3c34d;
    --vanilla-pack-edge: #e2ad36;
    --cocoa: #5a3418;
    --bear-light: #9a6640;
    --bear-dark: #6b4326;
    --cream: #fff4c8;
  }
  * { box-sizing: border-box; margin: 0; padding: 0; }
  html, body {
    width: 1200px; height: 900px; overflow: hidden;
    background: var(--canvas);
    font-family: "Fredoka", "Arial Rounded MT Bold", sans-serif;
    font-weight: 600;
  }
  .canvas { position: relative; width: 1200px; height: 900px; }

  .brand-name {
    position: absolute; left: 44px; top: 56px;
    display: flex; align-items: center; gap: 12px;
    font-size: 52px; line-height: 1; color: var(--cocoa);
  }
  .brand-name .dot {
    width: 26px; height: 26px; border-radius: 50%;
    background: var(--choc-pack);
  }

  .wrapper {
    position: absolute; top: 190px; width: 420px; height: 600px;
    border-radius: 22px;
    display: flex; flex-direction: column; align-items: center;
  }
  .wrapper::before, .wrapper::after {
    content: ""; position: absolute; left: 0; right: 0; height: 28px;
    background: var(--seal);
  }
  .wrapper::before { top: 0; border-radius: 22px 22px 0 0; }
  .wrapper::after { bottom: 0; border-radius: 0 0 22px 22px; }

  .wrapper--chocolate { left: 180px; background: var(--choc-pack); --seal: var(--choc-pack-edge); }
  .wrapper--vanilla { left: 654px; background: var(--vanilla-pack); --seal: var(--vanilla-pack-edge); }

  .mascot {
    margin-top: 56px; width: 220px; height: 160px;
    border-radius: 110px 110px 40px 40px;
    background: radial-gradient(circle at 50% 40%, var(--bear-light), var(--bear-dark));
  }
  .product-name {
    margin-top: 6px; text-align: center;
    font-size: 88px; line-height: 0.9; color: var(--cocoa);
  }
  .wrapper--chocolate .product-name { color: var(--cream); }
  .flavour {
    margin-top: 14px; font-size: 60px; line-height: 1;
    color: var(--cocoa);
  }

  .cookie-seal {
    position: absolute; right: 18px; bottom: 30px;
    width: 110px; height: 110px;
  }
  .cookie-seal text {
    font-family: "Fredoka", "Arial Rounded MT Bold", sans-serif;
    font-size: 12px; fill: var(--cocoa);
  }
</style>
</head>
<body>
<main class="canvas">
  <div class="brand-name"><span class="dot"></span>Zizi Otter</div>

  <section class="wrapper wrapper--chocolate">
    <div class="mascot" role="img" aria-label="Cute cartoon bear peeking over the product name"></div>
    <h2 class="product-name">Zizi<br>Otter</h2>
    <p class="flavour">chocolate</p>
    <svg class="cookie-seal" viewBox="0 0 130 130">
      <defs><path id="ring-choc" d="M65,65 m-50,0 a50,50 0 1,1 100,0 a50,50 0 1,1 -100,0"/></defs>
      <text><textPath href="#ring-choc" startOffset="50%">chocolate biscuit moles</textPath></text>
      <circle cx="65" cy="65" r="30" fill="var(--bear-dark)" role="img" aria-label="Bite-sized bear-shaped cookie"/>
    </svg>
  </section>

  <section class="wrapper wrapper--vanilla">
    <div class="mascot" role="img" aria-label="Cute cartoon bear peeking over the product name"></div>
    <h2 class="product-name">Zizi<br>Otter</h2>
    <p class="flavour">vanilla</p>
    <svg class="cookie-seal" viewBox="0 0 130 130">
      <defs><path id="ring-van" d="M65,65 m-50,0 a50,50 0 1,1 100,0 a50,50 0 1,1 -100,0"/></defs>
      <text><textPath href="#ring-van" startOffset="50%">vanilla biscuit moles</textPath></text>
      <circle cx="65" cy="65" r="30" fill="var(--bear-dark)" role="img" aria-label="Bite-sized bear-shaped cookie"/>
    </svg>
  </section>
</main>
</body>
</html>
```